Corvane Holdings , new business card design

investment firm with corporate clients . need double sided business card , vertical and horizontal options ,logo must be clear. prefer pantone colors only and sharp design. website also www.corvane-example.ae

Khalid Bin Rashed
Managing Director
Tel. +971 4 000 3829
Mobile +971 50 000 4172
khalid@corvane-example.ae
Palm Crest Tower, officw 18-B07, Qasr Gardens, Dubai

Contact Information for Business Card

Khalid Bin Rashed
Managing Director

Font styles to use
Serif

Colors

Designer to choose colors to be used in the design.

```html
<!DOCTYPE html>
<html lang="en">
<head>
<meta charset="utf-8">
<title>Corvane Holdings – Business Card</title>
<link rel="stylesheet" href="https://fonts.googleapis.com/css2?family=Tinos:wght@400;700&family=Open+Sans:wght@700&display=swap">
<style>
  :root {
    --stage: #9a9a9a;
    --paper: #ffffff;
    --ink: #0b0c10;
    --steel-blue: #4a7096;
    --sky-light: #8fb0d6;
    --sky-deep: #2d5a8c;
    --name-grey: #333333;
    --label-grey: #d4d4d4;
    --white: #ffffff;
  }
  html, body {
    margin: 0;
    padding: 0;
    width: 1200px;
    height: 1091px;
    overflow: hidden;
    background: var(--stage);
  }
  .presentation { display: block; width: 1200px; height: 1091px; }
  .side-label {
    font-family: "Open Sans", sans-serif;
    font-weight: 700;
    font-size: 26px;
    fill: var(--label-grey);
    letter-spacing: 0.5px;
  }
  .card { filter: drop-shadow(2px 3px 4px rgba(0,0,0,0.35)); }
  .card-paper { fill: var(--paper); }
  .ink-facet { fill: var(--ink); filter: drop-shadow(-3px -3px 5px rgba(0,0,0,0.35)); }
  .blue-facet { fill: var(--steel-blue); filter: drop-shadow(-3px 0 5px rgba(0,0,0,0.35)); }
  .wordmark {
    font-family: "Tinos", serif;
    font-weight: 400;
    font-size: 27px;
    fill: var(--ink);
    letter-spacing: 4px;
  }
  .serif-bold { font-family: "Tinos", serif; font-weight: 700; }
  .website { font-size: 17px; fill: var(--white); }
  .person-name { font-size: 19px; fill: var(--name-grey); }
  .person-role { font-size: 19px; fill: var(--steel-blue); }
  .contact-line { font-size: 17px; fill: var(--white); }
  .address-line { font-size: 13.5px; fill: var(--white); }
  .icon { fill: var(--white); }
</style>
</head>
<body>
<svg class="presentation" viewBox="0 0 1100 1000" width="1200" height="1091" xmlns="http://www.w3.org/2000/svg">
  <defs>
    <linearGradient id="sky" x1="0" y1="0" x2="0.6" y2="1">
      <stop offset="0" stop-color="var(--sky-light)"/>
      <stop offset="1" stop-color="var(--sky-deep)"/>
    </linearGradient>
  </defs>

  <text class="side-label" x="50" y="256">Front</text>
  <text class="side-label" x="66" y="722">Back</text>

  <!-- Front side -->
  <g class="card card-front">
    <rect class="card-paper" x="224" y="28" width="750" height="450"/>
    <polygon class="ink-facet" points="498,478 665,265 665,478"/>
    <rect class="blue-facet" x="665" y="28" width="309" height="450"/>
    <polygon points="668,28 974,28 974,478 958,478" fill="url(#sky)"
             role="img" aria-label="Photograph of a tall skyscraper against a blue sky"/>
    <polygon class="blue-facet" points="668,28 958,478 665,478 665,28"/>
    <text class="wordmark" x="292" y="238" textLength="288" lengthAdjust="spacing">CORVANE HOLDINGS</text>
    <text class="serif-bold website" x="796" y="453" text-anchor="middle">www.corvane-example.ae</text>
  </g>

  <!-- Back side -->
  <g class="card card-back">
    <rect class="card-paper" x="225" y="509" width="749" height="449"/>
    <polygon class="ink-facet" points="225,958 974,511 668,958"/>
    <polygon class="blue-facet" points="668,958 974,511 974,958"/>

    <text class="serif-bold person-name" x="313" y="617">Mr. Khalid Bin Rashed</text>
    <text class="serif-bold person-role" x="344" y="662">Managing Director</text>

    <g class="contact-icons">
      <path class="icon" d="M443,855 l4,-2 l4,6 l-3,2 q2,4 6,6 l2,-3 l6,4 l-2,4 q-6,2 -13,-6 q-6,-6 -4,-11z"/>
      <rect class="icon" x="445" y="875" width="13" height="20" rx="2"/>
      <rect x="447.5" y="878" width="8" height="12" fill="var(--ink)"/>
      <path class="icon" d="M441,901 h22 v12 h-22z"/>
      <path d="M441,901 l11,7 l11,-7" fill="none" stroke="var(--ink)" stroke-width="1.5"/>
    </g>
    <text class="serif-bold contact-line" x="483" y="867">+971 4 000 3829</text>
    <text class="serif-bold contact-line" x="483" y="889">+971 50 000 4172</text>
    <text class="serif-bold contact-line" x="483" y="911">khalid@corvane-example.ae</text>

    <text class="serif-bold address-line" x="748" y="866">Palm Crest Tower, officw 18-B07</text>
    <text class="serif-bold address-line" x="748" y="884">Qasr Gardens</text>
    <text class="serif-bold address-line" x="748" y="902">Dubai</text>
  </g>
</svg>
</body>
</html>
```